Schönheitssalon benötigt Flyer
Sehr schöne Arbeit, perfekt den Kundengeschmack getroffen. Leider zusätzliche Kosten durch (nicht enthaltene) Stockphotos, aber der Flyer ist sehr schick.
Zielgruppe
Ein Schönheitssalon in einer Pafümerie bietet diverse Angebote im Paket an (Gesichtsreinigung, Massage, Peeling, Maniküre, Sugaring). Vorrangig sollen Frauen angesprochen werden.
Aufgabenstellung
Faltblatt, gefalzt auf DIN A6 , 4-seiter
Endformat: 21,0 cm x 14,85 cm
gefalztes Endformat: 10,5 cm x 14,85 cm
Wir wünschen uns eine freundliche und helle Gestaltung mit rosé, voilett, pastell.
Das Grau, was jetzt gerade hinter dem Logo ist, wirkt sehr altbacken und nicht zeitgemäß.

```html
<!DOCTYPE html>
<html lang="de">
<head>
<meta charset="utf-8">
<title>Rosenzeit – Faltblatt</title>
<link href="https://fonts.googleapis.com/css2?family=Ubuntu:wght@400;500;700&display=swap" rel="stylesheet">
<style>
  :root {
    --bg: #5a5a5a;
    --paper: #ffffff;
    --lilac: #ecc6e0;
    --band: #d777aa;
    --band-dark: #c9609a;
    --accent: #e4507e;
    --wine: #8c0f3a;
    --ink: #3b3438;
    --row-tint: #f7e1ee;
    --rule: #d9779f;
  }
  * { box-sizing: border-box; margin: 0; padding: 0; }
  html, body { width: 1200px; height: 900px; overflow: hidden; }
  body {
    background: var(--bg);
    font-family: "Ubuntu", sans-serif;
    color: var(--ink);
    position: relative;
  }
  .page {
    position: absolute;
    top: 190px;
    width: 368px;
    height: 520px;
    background: var(--paper);
    overflow: hidden;
    box-shadow: 0 10px 30px rgba(0,0,0,.35);
  }
  .cover { left: 28px; }
  .spread {
    position: absolute; top: 190px; left: 436px;
    width: 736px; height: 520px;
    box-shadow: 0 10px 30px rgba(0,0,0,.35);
  }
  .spread .page { top: 0; box-shadow: none; }
  .inner-left { left: 0; }
  .inner-right { left: 368px; }
  .fold { position: absolute; left: 367px; top: 0; width: 2px; height: 520px;
    background: linear-gradient(to right, rgba(0,0,0,.08), rgba(0,0,0,0)); z-index: 5; }
  .shape { position: absolute; left: 0; width: 368px; }

  /* cover */
  .salon-name {
    position: absolute; top: 34px; left: 0; width: 100%;
    text-align: center; font-size: 34px; font-weight: 400; color: var(--ink);
    letter-spacing: 1px;
  }
  .portrait {
    position: absolute; left: 0; top: 96px; width: 236px; height: 330px;
    background: radial-gradient(ellipse at 45% 40%, #f3d0bd 0%, #e9b9a0 45%, #fbeee8 80%, #ffffff 100%);
  }
  .tagline {
    position: absolute; left: 226px; top: 200px; width: 142px;
    background: var(--accent); color: #fff;
    font-size: 12px; font-weight: 700; line-height: 1.2; padding: 6px 10px;
  }
  .location {
    position: absolute; left: 240px; top: 250px; font-size: 11px;
    color: var(--wine); line-height: 1.25;
  }
  .logo-name {
    position: absolute; left: 240px; top: 312px; font-size: 26px;
    font-weight: 700; color: var(--wine); letter-spacing: 1px;
  }
  .cover-info {
    position: absolute; bottom: 22px; color: #fff; font-size: 11px; line-height: 1.35;
  }
  .cover-info strong { display: block; font-size: 12px; }
  .contact { left: 22px; }
  .hours { left: 196px; }

  /* inner pages */
  .page-title {
    position: absolute; top: 40px; left: 24px; right: 20px;
    font-size: 19px; font-weight: 700; color: var(--wine);
  }
  .treatments { position: absolute; top: 82px; left: 24px; right: 22px; list-style: none; }
  .treatment { border-bottom: 1px solid var(--rule); padding: 5px 0 6px; position: relative; }
  .treatment:last-child { border-bottom: none; }
  .treatment h3 { font-size: 13px; font-weight: 700; color: var(--wine); }
  .treatment .duration { font-size: 10.5px; margin: 1px 0; }
  .treatment p { font-size: 9.5px; line-height: 1.3; padding-right: 48px; }
  .treatment .price {
    position: absolute; right: 0; bottom: 6px; font-size: 11.5px; font-weight: 700; color: var(--wine);
  }

  .extras { position: absolute; top: 80px; left: 20px; width: 328px; border-collapse: collapse; font-size: 9.5px; }
  .extras thead th {
    background: var(--wine); color: #fff; font-weight: 500; font-size: 10px;
    padding: 14px 4px 4px; text-align: center;
  }
  .extras thead th:first-child { text-align: left; }
  .extras td { padding: 3px 5px; border: 1px solid #ecc3d7; }
  .extras tbody tr:nth-child(odd) td { background: var(--row-tint); }
  .extras td.num { text-align: center; color: var(--wine); font-weight: 700; width: 58px; }

  .sugaring { position: absolute; top: 362px; left: 24px; width: 200px; }
  .sugaring h2 { font-size: 17px; font-weight: 700; color: var(--wine); margin-bottom: 6px; }
  .sugaring ul { list-style: none; font-size: 10.5px; line-height: 1.35; }
  .sugaring li { display: flex; justify-content: space-between; }
  .sugaring li span:last-child { color: var(--wine); font-weight: 700; }
  .sugaring .note { font-size: 9.5px; font-style: italic; margin-top: 6px; }
</style>
</head>
<body>

<section class="page cover">
  <svg class="shape" style="top:0" height="120" viewBox="0 0 368 120" preserveAspectRatio="none" aria-hidden="true">
    <path d="M0 0 H368 V96 Q190 70 0 110 Z" fill="var(--lilac)"/>
  </svg>
  <div class="portrait" role="img" aria-label="Porträtfoto einer jungen Frau mit Hochsteckfrisur und gepflegter Haut"></div>
  <h1 class="salon-name">Rosenzeit</h1>
  <div class="tagline">Entspannung<br>&amp; Kosmetik</div>
  <div class="location">Im Haus der<br>Stadt-Parfümerie<br>Hallberg</div>
  <div class="logo-name">LOGO</div>
  <svg class="shape" style="bottom:0" height="110" viewBox="0 0 368 110" preserveAspectRatio="none" aria-hidden="true">
    <path d="M0 40 Q200 -10 368 20 V110 H0 Z" fill="var(--band)"/>
  </svg>
  <div class="cover-info contact"><strong>Kontaktdaten:</strong>Mustermannstr. 5<br>12345 Musterstadt</div>
  <div class="cover-info hours"><strong>Öffnungszeiten:</strong>Do.: 9.30 – 19.00 Uhr<br>Fr.: 9.30 – 19.00 Uhr</div>
</section>

<div class="spread">
  <section class="page inner-left">
    <svg class="shape" style="top:0" height="40" viewBox="0 0 368 40" preserveAspectRatio="none" aria-hidden="true">
      <path d="M0 0 H368 V8 Q180 12 0 34 Z" fill="var(--lilac)"/>
    </svg>
    <h2 class="page-title">Gesichtsbehandlungen</h2>
    <ul class="treatments">
      <li class="treatment"><h3>Reinigungs-Behandlung</h3><div class="duration">ca. 60 Min.</div>
        <p>Reinigung, Peeling, Ausreinigung, Maske &amp; Abschlusspflege</p><span class="price">35,- €</span></li>
      <li class="treatment"><h3>Basis-Behandlung</h3><div class="duration">ca. 90 Min.</div>
        <p>Reinigung, Peeling, Ausreinigung, Augenbrauen-Korrektur, Massage &amp; Maske / leichtes Make-Up auf Wunsch</p><span class="price">49,- €</span></li>
      <li class="treatment"><h3>Intensiv-Behandlung</h3><div class="duration">ca. 90 Min.</div>
        <p>Reinigung, Peeling, Ausreinigung, Augenbrauen-Korrektur, Ampulle, Massage, Maske &amp; Augenmaske, leichtes Make-Up auf Wunsch</p><span class="price">59,- €</span></li>
      <li class="treatment"><h3>Verwöhn-Behandlung</h3><div class="duration">ca. 90 Min.</div>
        <p>Reinigung, Peeling, Ausreinigung, Augenbrauen-Korrektur, Ampulle, Massage, Maske, Hals- &amp; Dekolleté-Behandlung, leichtes Make-Up auf Wunsch</p><span class="price">67,- €</span></li>
      <li class="treatment"><h3>Luxus-Behandlung</h3><div class="duration">ca. 120 Min.</div>
        <p>Reinigung, Peeling, Ausreinigung, Augenbrauen-Korrektur, Ampulle, Massage, Vlies-Maske, Augenmaske, Lippenpackung, Handmassage &amp; Hals- &amp; Dekolleté-Behandlung, leichtes Make-Up auf Wunsch</p><span class="price">81,- €</span></li>
      <li class="treatment"><h3>Teenie-Behandlung (bis 18 Jahre)</h3><div class="duration">ca. 60 Min.</div>
        <p>Reinigung, Peeling, Ausreinigung &amp; Maske</p><span class="price">28,- €</span></li>
    </ul>
    <svg class="shape" style="bottom:0" height="30" viewBox="0 0 368 30" preserveAspectRatio="none" aria-hidden="true">
      <path d="M0 8 Q200 30 368 14 V30 H0 Z" fill="var(--band)"/>
    </svg>
  </section>

  <section class="page inner-right">
    <svg class="shape" style="top:0" height="40" viewBox="0 0 368 40" preserveAspectRatio="none" aria-hidden="true">
      <path d="M0 0 H368 V34 Q180 12 0 8 Z" fill="var(--lilac)"/>
    </svg>
    <h2 class="page-title" style="font-size:17px">Zusatz- &amp; Einzelbehandlungen</h2>
    <table class="extras">
      <thead><tr><th></th><th>Zusätzlich</th><th>Einzeln</th></tr></thead>
      <tbody>
        <tr><td>Augenbrauen zupfen/wachsen</td><td class="num">6,50 €</td><td class="num">8,- €</td></tr>
        <tr><td>Augenbrauen färben</td><td class="num">7,- €</td><td class="num">8,50 €</td></tr>
        <tr><td>Wimpern färben</td><td class="num"></td><td class="num">9,- €</td></tr>
        <tr><td>Augenbrauen &amp; Wimpern färben + zupfen</td><td class="num">22,- €</td><td class="num">21,- €</td></tr>
        <tr><td>Wimpernwelle</td><td class="num">28,- €</td><td class="num">32,- €</td></tr>
        <tr><td>Pflegende Maniküre (60 Min.)</td><td class="num">24,- €</td><td class="num">26,- €</td></tr>
        <tr><td>Pflegende Maniküre + Lack</td><td class="num"></td><td class="num">32,- €</td></tr>
        <tr><td>Wirkstoffampulle</td><td class="num"></td><td class="num">9,- €</td></tr>
        <tr><td>Tages-Make-Up</td><td class="num"></td><td class="num">25,- €</td></tr>
        <tr><td>Abend-/Foto-Make-Up</td><td class="num"></td><td class="num">35,- €</td></tr>
        <tr><td>Braut-Make-Up (inkl. Probe)</td><td class="num"></td><td class="num">70,- €</td></tr>
        <tr><td>Klassische Rückenmassage ca. 30 Min.</td><td class="num"></td><td class="num">25,- €</td></tr>
      </tbody>
    </table>
    <div class="sugaring">
      <h2>Sugaring</h2>
      <ul>
        <li><span>Oberlippe</span><span>9,- €</span></li>
        <li><span>Oberlippe + Kinn</span><span>14,- €</span></li>
        <li><span>Arme</span><span>ab 25,- €</span></li>
        <li><span>Beine Unterschenkel</span><span>23,- €</span></li>
        <li><span>Beine komplett</span><span>39,- €</span></li>
        <li><span>Rücken</span><span>ab 35,- €</span></li>
      </ul>
      <p class="note">(Andere Bereiche auf Anfrage!)</p>
    </div>
    <svg class="shape" style="bottom:0" height="30" viewBox="0 0 368 30" preserveAspectRatio="none" aria-hidden="true">
      <path d="M0 14 Q180 30 368 6 V30 H0 Z" fill="var(--band)"/>
    </svg>
  </section>
  <div class="fold"></div>
</div>

</body>
</html>
```